Business Card Design

Lotside Ledger is an online automotive resource on a national scale specifically targeting lease purchases for new cars. Our Online and app platform allow prospective lease clients to scan a window sticker while at a franchise dealership and instantly receive a lease quote at what we call the sweet spot. Lotside Ledger offers price transparency during the lease process to allow average people the confidence in the lease process and takes away any fear of the big franchise dealers.
Lotside ledger allows ordinary lease customers to know they are getting a low price lease and not overpaying. Never overpay again

Industry/Entity Type

Automotive

Contact Information for Business Card

Lotside Ledger
Marcus Todwell (President of operations)
Phone: 888-302-7716
Cell: 561-448-2053

```html
<!DOCTYPE html>
<html lang="en">
<head>
<meta charset="utf-8">
<title>Lotside Ledger — Business Card</title>
<link rel="stylesheet" href="https://fonts.googleapis.com/css2?family=Montserrat:wght@400;600;800&display=swap">
<style>
  :root {
    --backdrop: #161618;
    --card: #27282c;
    --ink: #d9dadc;
    --ink-bright: #f4f4f5;
    --accent: #1f89bd;
    --muted: #a9abb0;
  }
  * { box-sizing: border-box; margin: 0; padding: 0; }
  html, body {
    width: 1200px; height: 900px; overflow: hidden;
    background: var(--backdrop);
    font-family: "Montserrat", Arial, sans-serif;
  }
  .sheet {
    width: 1200px; height: 900px;
    display: flex; flex-direction: column; align-items: center; justify-content: center;
    gap: 36px;
  }
  .card {
    position: relative;
    width: 700px; height: 400px;
    background: var(--card);
    border-radius: 26px;
    color: var(--ink);
  }
  /* back side */
  .card--back {
    display: flex; flex-direction: column; align-items: center; justify-content: center;
    gap: 22px;
  }
  .brand-mark {
    display: flex; align-items: center; gap: 14px;
  }
  .brand-mark__dot {
    width: 22px; height: 22px; border-radius: 50%; background: var(--ink-bright);
  }
  .brand-mark__name {
    font-weight: 800; color: var(--ink-bright); text-transform: uppercase;
    letter-spacing: -0.5px; line-height: 0.95;
  }
  .card--back .brand-mark__name { font-size: 46px; }
  .website { font-size: 15px; letter-spacing: 0.5px; color: var(--ink); }
  .website__domain { color: var(--accent); }

  /* front side */
  .card--front .brand-mark {
    position: absolute; left: 56px; top: 84px;
  }
  .card--front .brand-mark__name { font-size: 40px; }
  .contact {
    position: absolute; left: 92px; bottom: 62px;
    font-size: 17px; line-height: 1.35;
  }
  .contact__name { color: var(--accent); font-weight: 600; }
  .contact__role { color: var(--ink); margin-bottom: 16px; }
  .contact__row { display: flex; gap: 12px; }
  .contact__label { color: var(--accent); width: 62px; }
  .contact__value { color: var(--ink); letter-spacing: 0.4px; }
  .address {
    position: absolute; left: 430px; top: 218px;
    font-size: 16px; line-height: 1.45; color: var(--muted);
  }
</style>
</head>
<body>
  <main class="sheet">
    <section class="card card--back" aria-label="Card back">
      <div class="brand-mark">
        <span class="brand-mark__dot"></span>
        <span class="brand-mark__name">Lotside Ledger</span>
      </div>
      <p class="website">www.<span class="website__domain">lotsideledger</span>.com</p>
    </section>

    <section class="card card--front" aria-label="Card front">
      <div class="brand-mark">
        <span class="brand-mark__dot"></span>
        <span class="brand-mark__name">Lotside<br>Ledger</span>
      </div>

      <div class="contact">
        <p class="contact__name">Marcus Todwell</p>
        <p class="contact__role">President of operations</p>
        <p class="contact__row"><span class="contact__label">Phone</span><span class="contact__value">888-302-7716</span></p>
        <p class="contact__row"><span class="contact__label">Cell</span><span class="contact__value">561-448-2053</span></p>
      </div>

      <address class="address" style="font-style: normal;">
        4870 Harbor Mill Rd Suite 12<br>
        Palm Vista, FL 33410
      </address>
    </section>
  </main>
</body>
</html>
```